Yard sign design for high end luxury home builder.

Need a design for signage on custom homes that are being built. I already have a logo that I am satisfied with that needs to be incorporated. I need the following incorporated in the design of the sign-
- Lic number 582316
- phone number (805) 471-2938‬
- tembleyhomeworks.com
- Logo/Branding

If possible it may be nice to have the following quote that is on are business cards-

Quote from Corwin of Valdema-
HE WHO WORKS WITH HIS HANDS IS A LABORER.
HE WHO WORKS WITH HIS HANDS & HIS HEAD IS A CRAFTSMAN.
HE WHO WORKS WITH HIS HANDS & HIS HEAD & HIS HEART IS AN ARTISAN.
-CORWIN OF VALDEMA

Target Market(s)

Archetect, Designers, Clients desiring to build a new home or remodel.

Colors
fde9d4
fee4d5
fabb94
fac994
faa54b
f68d4d
f37122
f78f20
f68e4e

Requirements
Must have
• - Lic number 582316
• - phone number (805) 471-2938‬
• - tembleyhomeworks.com
• - Logo/Branding
Nice to have
• Quote from Corwin of Valdema-
• HE WHO WORKS WITH HIS HANDS IS A LABORER.
• HE WHO WORKS WITH HIS HANDS & HIS HEAD IS A CRAFTSMAN.
• HE WHO WORKS WITH HIS HANDS & HIS HEAD & HIS HEART IS AN ARTISAN.
• -CORWIN OF VALDEMA
• OR the below statement-
• Craftsmen that Care
Should not have
• Any additional verbiage not specified above including any type of verbiage about what kind of company we are. For instance- Integrity, reputable... It's just all played out. Im just looking for a bitching design that has the info that compliments my logo/branding.

```html
<!DOCTYPE html>
<html lang="en">
<head>
<meta charset="utf-8">
<title>Tembley Homeworks – Yard Sign</title>
<link href="https://fonts.googleapis.com/css2?family=PT+Serif:wght@400;700&display=swap" rel="stylesheet">
<style>
  :root {
    --tan: #9e8669;
    --ink: #1b1b1b;
    --paper: #eef0ef;
    --page: #ffffff;
    --white: #ffffff;
  }
  * { margin: 0; padding: 0; box-sizing: border-box; }
  html, body {
    width: 1200px;
    height: 1200px;
    overflow: hidden;
    background: var(--page);
    font-family: "PT Serif", Georgia, serif;
  }
  .sign {
    position: absolute;
    left: 247px;
    width: 697px;
    height: 522px;
    color: var(--tan);
    overflow: hidden;
  }
  .sign--dark { top: 56px; background: var(--ink); }
  .sign--light { top: 610px; background: var(--paper); }

  .sign__frame {
    position: absolute;
    inset: 10px;
    border: 2px solid var(--tan);
  }

  .brand {
    position: absolute;
    left: 53px;
    top: 54px;
    width: 228px;
    text-align: center;
  }
  .brand__mark {
    display: block;
    width: 190px;
    height: 190px;
    margin: 0 auto 16px;
    background: var(--tan);
  }
  .brand__name {
    font-weight: 700;
    font-size: 30px;
    line-height: 34px;
    color: var(--tan);
    text-transform: uppercase;
    letter-spacing: 1px;
  }

  .headline {
    position: absolute;
    left: 338px;
    top: 44px;
    font-weight: 400;
    font-size: 70px;
    line-height: 66px;
    letter-spacing: -0.5px;
  }

  .quote {
    position: absolute;
    left: 349px;
    top: 198px;
    width: 320px;
    font-size: 15px;
    line-height: 18px;
  }
  .quote__open,
  .quote__close {
    font-size: 34px;
    font-weight: 700;
    line-height: 0;
  }
  .quote__open {
    position: absolute;
    left: -26px;
    top: 14px;
  }
  .quote__close {
    position: relative;
    top: 12px;
    left: 4px;
  }
  .quote strong { font-weight: 700; }
  .quote__rule {
    width: 142px;
    height: 1px;
    margin: 8px 0 8px;
    background: var(--tan);
  }
  .quote__author {
    font-weight: 700;
    font-style: normal;
    font-size: 14px;
  }

  .phone {
    position: absolute;
    left: 48px;
    top: 340px;
    width: 604px;
    font-size: 93px;
    line-height: 100px;
    font-weight: 400;
    letter-spacing: -1px;
    white-space: nowrap;
    text-align: center;
  }

  .web {
    position: absolute;
    left: 181px;
    top: 466px;
    width: 334px;
    height: 46px;
    border-radius: 16px 16px 0 0;
    background: var(--tan);
    font-size: 24px;
    line-height: 44px;
    text-align: center;
  }
  .sign--dark .web { color: var(--ink); }
  .sign--light .web { color: var(--white); }

  .licence {
    position: absolute;
    left: 569px;
    top: 482px;
    font-size: 13px;
    font-weight: 700;
  }
</style>
</head>
<body>

<section class="sign sign--dark">
  <div class="sign__frame"></div>
  <div class="brand">
    <span class="brand__mark"></span>
    <div class="brand__name">Tembley<br>Homeworks</div>
  </div>
  <h1 class="headline">Craftsmen<br>That Care</h1>
  <blockquote class="quote">
    <span class="quote__open">“</span>
    He who works with his hands is a <strong>laborer</strong>.<br>
    He who works with his hands &amp; his head<br>
    is a <strong>craftsman</strong>.<br>
    He who works with his hands &amp; his head<br>
    &amp; his heart is an <strong>artisan</strong>.<span class="quote__close">”</span>
    <div class="quote__rule"></div>
    <cite class="quote__author">Corwin of Valdema</cite>
  </blockquote>
  <div class="phone">(805) 471-2938</div>
  <div class="web">tembleyhomeworks.com</div>
  <div class="licence">Lic 582316</div>
</section>

<section class="sign sign--light">
  <div class="sign__frame"></div>
  <div class="brand">
    <span class="brand__mark"></span>
    <div class="brand__name">Tembley<br>Homeworks</div>
  </div>
  <h2 class="headline">Craftsmen<br>That Care</h2>
  <blockquote class="quote">
    <span class="quote__open">“</span>
    He who works with his hands is a <strong>laborer</strong>.<br>
    He who works with his hands &amp; his head<br>
    is a <strong>craftsman</strong>.<br>
    He who works with his hands &amp; his head<br>
    &amp; his heart is an <strong>artisan</strong>.<span class="quote__close">”</span>
    <div class="quote__rule"></div>
    <cite class="quote__author">Corwin of Valdema</cite>
  </blockquote>
  <div class="phone">(805) 471-2938</div>
  <div class="web">tembleyhomeworks.com</div>
  <div class="licence">Lic 582316</div>
</section>

</body>
</html>
```